Corrigan Construction Law P.A.

Business Card with Corporate Logo. For a law firm specializing in construction law.

need address, telephone, email and website. Also, have an elegant and conservative logo.

Logo so it is RBN.

Full name "Gordon T. Corrigan

Under my name title "Attorney at Law"

Under title "Board Certified in Construction Law"

PA in email is lower case

Add logo to back side of card

Mix in a bit of gold color into card to go with the green

Some color on bottom
Updates

Target Market(s)

legal

Industry/Entity Type

Construction

Contact Information for Business Card

I like it -- edits: 1. add "L" to logo so it is RBN. 2. add my full name "Gordon T. Business Card with Corporate Logo. For a law firm specializing in construction law.

Logo so it is RBN.

PA in email is lower case

Font styles to use
Serif

Colors
00a990
f78f20

Requirements
Must have
• Conservative legal designed logo for construction market
• Address:
• Corrigan Construction Law, P.A.
• 4150 Meadowlark Ave North, Ste B4
• Jacksonville, Florida 32217
• Main: 904-555-3172
• Direct: 904-555-8410
• Fax: 904-555-8410
• gt@corriganpa-example.com
• www.corriganbuildlaw-example.com
Nice to have
• Catchy conservative logo on card
Should not have
• Flashy

```html
<!DOCTYPE html>
<html lang="en">
<head>
<meta charset="utf-8">
<title>Corrigan Construction Law P.A. – Business Card</title>
<link rel="stylesheet" href="https://fonts.googleapis.com/css2?family=Rosarivo&family=PT+Sans&display=swap">
<style>
  :root {
    --page: #ffffff;
    --card-green: #256b27;
    --card-glow: #2f7a31;
    --gold: #f3a91f;
    --ink-light: #ffffff;
    --ink-dark: #1a1a1a;
    --icon-green: #2a6b2a;
    --band: #ffffff;
    --shadow: rgba(0, 0, 0, 0.45);
  }
  * { margin: 0; padding: 0; box-sizing: border-box; }
  html, body {
    width: 1200px; height: 1177px; overflow: hidden;
    background: var(--page);
  }
  .canvas { position: relative; width: 1200px; height: 1177px; }

  .card {
    position: absolute;
    background: var(--card-green);
    box-shadow: 6px 8px 10px var(--shadow);
    overflow: hidden;
  }
  .card--front { left: 15px; top: 15px; width: 1142px; height: 540px; }
  .card--back {
    left: 18px; top: 593px; width: 1141px; height: 541px;
    background: radial-gradient(circle at 52% 33%, var(--card-glow) 0%, var(--card-green) 38%);
  }

  .serif { font-family: "Rosarivo", Georgia, serif; color: var(--ink-light); position: absolute; white-space: nowrap; }

  .brand-mark {
    position: absolute;
    font-family: "Rosarivo", Georgia, serif;
    color: var(--gold);
    font-size: 72px;
    line-height: 1;
    letter-spacing: 2px;
    transform: translateX(-50%);
  }
  .card--front .brand-mark { left: 601px; top: 70px; }
  .card--back .brand-mark { left: 573px; top: 80px; }

  .attorney-name { left: 601px; top: 193px; font-size: 43px; transform: translateX(-50%); }
  .name-rule {
    position: absolute; left: 383px; top: 240px; width: 437px; height: 1px;
    background: rgba(255, 255, 255, 0.7);
  }
  .attorney-title { left: 575px; top: 242px; font-size: 30px; transform: translateX(-50%); }
  .certification { left: 563px; top: 300px; font-size: 38px; transform: translateX(-50%); }

  .contact-band {
    position: absolute; left: 5px; right: 0; top: 380px; height: 115px;
    background: var(--band);
  }
  .contact-item {
    position: absolute;
    display: flex; align-items: center; gap: 16px;
    font-family: "PT Sans", Arial, sans-serif;
    font-size: 19px; color: var(--ink-dark);
    white-space: nowrap;
  }
  .contact-item svg { flex: none; }
  .contact-item--address { left: 50px; top: 24px; }
  .contact-item--phone   { left: 50px; top: 64px; }
  .contact-item--web     { left: 647px; top: 22px; }
  .contact-item--email   { left: 647px; top: 64px; }

  .firm-name { left: 601px; top: 232px; font-size: 49px; transform: translateX(-50%); }
</style>
</head>
<body>
<main class="canvas">

  <section class="card card--front" aria-label="Card front">
    <div class="brand-mark">RBN</div>
    <h1 class="serif attorney-name" style="font-weight:400">Gordon T. Corrigan</h1>
    <div class="name-rule"></div>
    <p class="serif attorney-title">Attorney at Law</p>
    <p class="serif certification">Board Certified in Construction Law</p>

    <div class="contact-band">
      <div class="contact-item contact-item--address">
        <svg width="56" height="26" viewBox="0 0 56 26" aria-hidden="true">
          <path d="M2 14 L28 2 L54 14 L48 14 L28 6 L8 14 Z" fill="var(--icon-green)"/>
          <path d="M12 14 L28 8 L44 14 L44 25 L33 25 L33 18 L23 18 L23 25 L12 25 Z" fill="var(--icon-green)"/>
        </svg>
        <span>Company Location/address</span>
      </div>
      <div class="contact-item contact-item--phone">
        <svg width="56" height="26" viewBox="0 0 56 26" aria-hidden="true">
          <path d="M6 22 C2 18 4 12 10 12 L14 16 C20 10 34 6 44 6 L46 2 C52 2 55 8 50 12 L44 12 C34 12 22 14 16 22 Z" fill="var(--icon-green)"/>
        </svg>
        <span>Company&nbsp; phone number/ contact number</span>
      </div>
      <div class="contact-item contact-item--web">
        <svg width="48" height="34" viewBox="0 0 48 34" aria-hidden="true">
          <rect x="1" y="1" width="46" height="32" fill="none" stroke="var(--icon-green)" stroke-width="2"/>
          <circle cx="24" cy="17" r="11" fill="none" stroke="var(--icon-green)" stroke-width="2"/>
          <ellipse cx="24" cy="17" rx="5" ry="11" fill="none" stroke="var(--icon-green)" stroke-width="1.6"/>
          <line x1="13" y1="17" x2="35" y2="17" stroke="var(--icon-green)" stroke-width="1.6"/>
          <line x1="15" y1="11" x2="33" y2="11" stroke="var(--icon-green)" stroke-width="1.4"/>
          <line x1="15" y1="23" x2="33" y2="23" stroke="var(--icon-green)" stroke-width="1.4"/>
        </svg>
        <span style="margin-left:32px">Company Website</span>
      </div>
      <div class="contact-item contact-item--email">
        <svg width="48" height="26" viewBox="0 0 48 26" aria-hidden="true">
          <rect x="5" y="4" width="38" height="20" fill="var(--icon-green)"/>
          <path d="M5 4 L24 16 L43 4" fill="none" stroke="var(--band)" stroke-width="1.6"/>
        </svg>
        <span style="margin-left:32px">Corrigan Construction Law p.a.</span>
      </div>
    </div>
  </section>

  <section class="card card--back" aria-label="Card back">
    <div class="brand-mark">RBN</div>
    <h2 class="serif firm-name" style="font-weight:400">Corrigan Construction Law P.A.</h2>
  </section>

</main>
</body>
</html>
```